Aviation Maintenance & Aircraft Cleaning Website

We need a fairly simple modern sleek website . Our company does aviation maintenance , aircraft cleaning , maintenance tracking . We work on KT420 HELICOPTERS , BELVANKO T82 HELICOPTERS , MORVELL TARRANT 512 HELICOPTERS. We would like a website that can be mobile as well with future ideas that an app where you could book cleanings and maintenance . Right now the biggest thing is for our customer to see a website , be able to book our services online and see our staff . the website must be modern and clean .

Target Market(s)

Aviation maintenance , aviation cleaning ,

Logo Text

TW but 1 image unlike the one i uploaded which is two . Im open for different aviation designs

Number of Pages Required

5+ page

Font styles to use
Serif

Requirements
Must have
• Home page , Aircraft Maintenance , Aircraft Cleaning , About Us , Contact , Careers

TW Aviation is insured and all of our mechanics are licensed by the NQB with an Airframe & Powerplant rating. ( FRONT PAGE )

Home page should have a simple nice picture of a KT420 or Belvanko T82 . My Logo as you can see seems like two logos . i would like 1 logo and made of the two if possible . (New ideas are welcome . )

Book a Cleaning Calendar should in the aircraft cleaning page . The aircraft cleaning page should have a picture of cleaning a helicopter or private jet .

Aircraft maintenance page should have a mechanic working on a helicopter . The Page should have a fast way to contact us .

We are a mobile AOG team who is available 24/7 . What we do
Scheduled & Unscheduled aircraft maintenance
Major & Minor repairs
STC installations
Aircraft Weight & Balance
Aircraft Painting
Aircraft Cleaning
Maintenance Tracking Utilizing Tracking Programs or spreadsheets
Removal & Installation of Components
Aircraft Pre Buy Inspections
Nice to have
• modern , sleek , aviation

Meet the Staff

Picture with Headset on flying in a helicopter

CEO Mateus Ferreira

Mateus Has been an aircraft mechanic for over 10 years . He has worked for the largest sightseeing & charter tourism company in the New York City area as well as repair stations & manufacturers. He has aircraft specific training to the Kestrane KT420 & Vornel 2K4. He has worked on several airframes including the Belvanko T82 and the Morvell 512. He has held every position in an aircraft maintenance department from mechanic up to Director of Maintenance . His work ethic and ability to manage mechanics in a organized and structured way gives any department or inspection a clear direction .

About Us

TW Aviation Services is company with aircraft maintenance experience . We focus on inspections of aircraft . Our Aircraft Mechanics who are pilots and IA's have experience many aircraft but specialize in the Kestrane KT420 , KT425 , KT435 . The Belvanko T82 and Morvell Tarrant 512 . Our focus is safety and to maintain aircraft day in and day out so our customer can operate the aircraft safely while keeping up with all the manufacturers inspections .

We know aircraft maintenance & maintenance planning . Leave the technical and tedious things to us . Get in your aircraft and fly knowing you have the best maintenance crew in the business.

```html
<!DOCTYPE html>
<html lang="en">
<head>
<meta charset="utf-8">
<title>About Us – TW Aviation</title>
<link rel="stylesheet" href="https://fonts.googleapis.com/css2?family=Montserrat:wght@400;500;600;700&family=Playfair+Display:wght@700;800&display=swap">
<style>
:root{
  --blue:#1a48a0;
  --navy:#0d1427;
  --ink:#111a2e;
  --text:#2b2f3a;
  --faint:#e8edf6;
  --white:#ffffff;
  --footer-link:#d7dbe4;
}
*{margin:0;padding:0;box-sizing:border-box}
html,body{width:798px;height:1200px;overflow:hidden;background:var(--white)}
body{position:relative;font-family:"Montserrat",sans-serif;color:var(--text)}
a{text-decoration:none}
.abs{position:absolute}

.site-header{left:0;top:0;width:798px;height:44px;background:var(--white)}
.brand{left:81px;top:5px;width:46px;text-align:center;color:var(--blue)}
.brand-mark{display:block;font-family:"Montserrat",sans-serif;font-weight:700;font-size:19px;line-height:20px;letter-spacing:1px}
.brand-sub{display:block;font-family:"Montserrat",sans-serif;font-weight:700;font-size:5px;letter-spacing:1.4px;margin-top:1px}
.main-nav a{position:absolute;top:16px;font-size:10px;color:#333}
.main-nav a.current{color:var(--blue);border-bottom:1px solid var(--blue);padding-bottom:2px}
.contact-btn{left:634px;top:11px;width:81px;height:23px;background:var(--blue);color:var(--white);font-size:10px;line-height:23px;text-align:center}

.page-banner{left:0;top:44px;width:798px;height:100px;background:var(--blue)}
.page-title{left:83px;top:98px;font-family:"Playfair Display",serif;font-weight:700;font-size:20px;color:var(--white)}
.breadcrumb{left:655px;top:134px;font-size:6px;color:#c8d4ee}
.breadcrumb b{color:var(--white);font-weight:600}

.watermark{left:-10px;top:150px;font-family:"Montserrat",sans-serif;font-weight:700;font-size:260px;line-height:280px;color:var(--faint);letter-spacing:-10px}
.who-title{left:178px;top:246px;font-family:"Playfair Display",serif;font-weight:800;font-size:30px;line-height:36px;color:var(--ink)}
.rule{height:1.5px;background:var(--ink)}
.who-copy{left:301px;top:230px;width:300px;font-size:7.8px;line-height:13.9px;color:var(--text)}
.who-copy p+p{margin-top:10px}

.staff-title{left:0;top:480px;width:798px;text-align:center;font-family:"Playfair Display",serif;font-weight:800;font-size:30px;color:var(--ink)}

.staff-band{left:0;top:640px;width:798px;height:342px;background:var(--navy)}
.portrait-frame{left:295px;top:538px;width:208px;height:208px;border-radius:50%;background:var(--white)}
.portrait{left:301px;top:542px;width:196px;height:196px;border-radius:50%;background:radial-gradient(circle at 45% 40%,#7b7f84 0%,#4b4f55 45%,#2f3338 100%)}
.staff-name{left:0;top:756px;width:798px;text-align:center;font-size:13px;font-weight:600;color:var(--white);letter-spacing:.4px}
.bio-card{left:166px;top:781px;width:466px;height:107px;border-radius:7px;background:var(--blue);padding:11px 18px 0 25px;font-size:7.9px;line-height:13.9px;color:var(--white);letter-spacing:.1px}

.cta-band{left:0;top:982px;width:798px;height:41px;background:var(--blue)}
.site-footer{left:0;top:1023px;width:798px;height:177px;background:var(--navy)}
.footer-brand{left:80px;top:1047px;width:70px;text-align:center;color:var(--white)}
.footer-brand .brand-mark{font-size:32px;line-height:32px}
.footer-brand .brand-sub{font-size:8px;letter-spacing:2.2px}
.contact-line{left:85px;font-size:9.5px;font-weight:500;color:var(--white);display:flex;align-items:center;gap:6px}
.socials{left:88px;top:1157px;display:flex;gap:20px}
.socials span{width:13px;height:13px;border-radius:50%;border:1.5px solid var(--white)}
.footer-col{font-size:10px;color:var(--white)}
.footer-col h3{font-size:10px;font-weight:600;color:var(--white);margin-bottom:15px}
.footer-col a{display:block;color:var(--footer-link);margin-bottom:16px}
.copyright{left:715px;top:1173px;font-size:6.5px;color:#c7ccd6}
</style>
</head>
<body>

<header class="abs site-header">
  <div class="abs brand"><span class="brand-mark">TW</span><span class="brand-sub">AVIATION</span></div>
  <nav class="main-nav">
    <a style="left:239px" href="#">Home</a>
    <a class="current" style="left:303px" href="#">About Us</a>
    <a style="left:383px" href="#">Maintenance</a>
    <a style="left:482px" href="#">Cleaning</a>
    <a style="left:560px" href="#">Careers</a>
  </nav>
  <a class="abs contact-btn" href="#">Contact Us</a>
</header>

<section class="abs page-banner"></section>
<h1 class="abs page-title">About Us</h1>
<div class="abs breadcrumb">Home &gt; <b>About Us</b></div>

<div class="abs watermark" aria-hidden="true">TW</div>
<h2 class="abs who-title">Who<br>We Are</h2>
<div class="abs rule" style="left:193px;top:322px;width:90px"></div>
<div class="abs rule" style="left:178px;top:331px;width:94px"></div>
<div class="abs who-copy">
  <p>TW Aviation Services is a company with aircraft maintenance experience. We focus on inspections of aircraft. Our Aircraft Mechanics who are pilots and IA's have experienced many aircraft but specialize in the Kestrane KT420, KT425, KT435. The Belvanko T82 and Morvell Tarrant 512. Our focus is safety and to maintain aircraft day in and day out so our customers can operate the aircraft safely while keeping up with all the manufacturer's inspections.</p>
  <p>We know aircraft maintenance &amp; maintenance planning. Leave the technical and tedious things to us. Get in your aircraft and fly knowing you have the best maintenance crew in the business.</p>
</div>

<h2 class="abs staff-title">Meet the Staff</h2>
<div class="abs rule" style="left:190px;top:502px;width:99px"></div>
<div class="abs rule" style="left:509px;top:502px;width:99px"></div>

<section class="abs staff-band"></section>
<div class="abs portrait-frame"></div>
<div class="abs portrait" role="img" aria-label="Photo of the CEO wearing a headset while flying in a helicopter"></div>
<h3 class="abs staff-name">CEO Mateus Ferreira</h3>
<div class="abs bio-card">Mateus has been an aircraft mechanic for over 10 years. He has worked for the largest sightseeing &amp; charter tourism company in the New York City area as well as repair stations &amp; manufacturers. He has aircraft-specific training in the Kestrane KT420 &amp; Vornel 2K4. He has worked on several airframes including the Belvanko T82 and the Morvell 512. He has held every position in an aircraft maintenance department from mechanic up to Director of Maintenance. His work ethic and ability to manage mechanics in an organized and structured way give any department or inspection a clear direction.</div>

<section class="abs cta-band"></section>
<svg class="abs" style="left:673px;top:1001px" width="42" height="22" viewBox="0 0 42 22" aria-hidden="true"><polygon points="0,22 21,0 42,22" fill="#ffffff"/></svg>

<footer class="abs site-footer"></footer>
<div class="abs footer-brand"><span class="brand-mark">TW</span><span class="brand-sub">AVIATION</span></div>
<div class="abs contact-line" style="top:1112px">
  <svg width="11" height="11" viewBox="0 0 24 24" aria-hidden="true"><path fill="#fff" d="M6.6 10.8a15.1 15.1 0 006.6 6.6l2.2-2.2c.3-.3.7-.4 1-.2 1.1.4 2.3.6 3.6.6.6 0 1 .4 1 1V20c0 .6-.4 1-1 1A17 17 0 013 4c0-.6.4-1 1-1h3.5c.6 0 1 .4 1 1 0 1.3.2 2.5.6 3.6.1.3 0 .7-.2 1z"/></svg>
  <span>+555 010 2030</span>
</div>
<div class="abs contact-line" style="top:1135px">
  <svg width="12" height="10" viewBox="0 0 24 20" aria-hidden="true"><rect x="0" y="0" width="24" height="20" rx="2" fill="#fff"/><path d="M2 3l10 7 10-7" stroke="#0d1427" stroke-width="2" fill="none"/></svg>
  <span>hello@twaviation.net</span>
</div>
<div class="abs socials" aria-label="Social links"><span></span><span></span><span></span></div>

<div class="abs footer-col" style="left:297px;top:1075px"><h3>About Us</h3><a href="#">Meet Our Staff</a><a href="#">Career</a></div>
<div class="abs footer-col" style="left:438px;top:1075px"><h3>Contact Us</h3><a href="#">FAQ</a><a href="#">Blog</a></div>
<div class="abs footer-col" style="left:554px;top:1075px"><h3>Support</h3><a href="#">Services</a><a href="#">Procedures</a></div>
<div class="abs copyright">©2020 TW AVIATION</div>

</body>
</html>
```